Business Card Design

We are a Sydney based bespoke Concierge company, providing hospitality services including Concierge staffing, catering, home dining, events, delivery, stallorix, and manage desks in residential apartment services. Our website goes into more detail.

Target Market(s)

corporate clients, upscale residential clients, executives,

Industry/Entity Type

Hospitality

Contact Information for Business Card

David SouthwellDirector of Operations & Customer Experience
Marlowe Concierge
W:www.marloweconcierge-demo.net;
E;peter@marloweconcierge-demo.net
M: 0412 907 281

Font styles to use
Serif

Colors
3176b5
85cae6
d2a4cc
6b449b

Requirements
Must have
• Business name
• Name
• Title
• Tel
• Email
• Website
Nice to have
• Back - facebook , twitter, instagram

```html
<!DOCTYPE html>
<html lang="en">
<head>
<meta charset="utf-8">
<title>Marlowe Concierge – Business Card</title>
<link rel="stylesheet" href="https://fonts.googleapis.com/css2?family=Source+Serif+4:wght@300;400&display=swap">
<style>
  :root {
    --page: #ffffff;
    --bleed-line: #e4262b;
    --trim-line: #1aa1db;
    --panel: #ebeceb;
    --band: #ffffff;
    --accent: #3176b5;
    --accent-soft: #85cae6;
    --ink: #2b2b2b;
  }
  html, body {
    margin: 0;
    padding: 0;
    overflow: hidden;
    background: var(--page);
  }
  .card-canvas {
    position: relative;
    width: 1200px;
    height: 742px;
    background: var(--page);
    font-family: "Source Serif 4", Georgia, serif;
    font-weight: 300;
    color: var(--ink);
    overflow: hidden;
  }
  .bleed-guide, .trim-guide {
    position: absolute;
    box-sizing: border-box;
  }
  .bleed-guide {
    left: 18px; top: 19px; width: 1161px; height: 700px;
    border: 3px solid var(--bleed-line);
  }
  .trim-guide {
    left: 44px; top: 45px; width: 1111px; height: 651px;
    border: 3px solid var(--trim-line);
  }
  .card-panel {
    position: absolute;
    left: 67px; top: 65px; width: 810px; height: 611px;
    background: var(--panel);
  }
  .accent-column {
    position: absolute;
    left: 877px; top: 65px; width: 255px; height: 611px;
    background: var(--accent);
  }
  .light-band {
    position: absolute;
    left: 67px; top: 323px; width: 810px; height: 94px;
    background: var(--band);
  }
  .lounge-photo {
    position: absolute;
    left: 877px; top: 323px; width: 255px; height: 94px;
    background: linear-gradient(90deg, #c9cfcf 0%, #f4f5f3 35%, #e9ecea 60%, #b7c6c4 100%);
  }
  .identity {
    position: absolute;
    left: 202px; top: 116px;
  }
  .identity .person-name {
    margin: 0;
    font-size: 28px;
    line-height: 34px;
    font-weight: 400;
  }
  .identity .person-title {
    margin: 0;
    font-size: 16.5px;
    line-height: 24px;
  }
  .identity .company-name {
    margin: 0;
    font-size: 20px;
    line-height: 28px;
  }
  .brand-mark {
    position: absolute;
    left: 202px; top: 320px;
    display: flex;
    align-items: center;
    gap: 22px;
  }
  .brand-mark .brand-square {
    width: 40px;
    height: 40px;
    background: var(--accent);
    flex: none;
  }
  .brand-mark .brand-name {
    margin: 0;
    font-size: 46px;
    line-height: 50px;
    font-weight: 300;
    color: var(--ink);
    white-space: nowrap;
  }
  .contact-list {
    position: absolute;
    left: 202px; top: 522px;
    margin: 0; padding: 0;
    list-style: none;
    font-size: 20px;
    line-height: 27px;
  }
  .contact-list .label {
    display: inline-block;
    width: 28px;
  }
</style>
</head>
<body>
  <main class="card-canvas">
    <div class="bleed-guide"></div>
    <div class="trim-guide"></div>

    <div class="card-panel"></div>
    <div class="accent-column"></div>
    <div class="light-band"></div>
    <div class="lounge-photo" role="img" aria-label="Photo of a bright apartment lounge with a white sofa and coffee table by large windows"></div>

    <section class="identity">
      <p class="person-name">Peter Hollingby</p>
      <p class="person-title">Director of Operations &amp; Customer Experience</p>
      <p class="company-name">Marlowe Concierge</p>
    </section>

    <div class="brand-mark">
      <span class="brand-square"></span>
      <p class="brand-name">MARLOWE<br>CONCIERGE</p>
    </div>

    <ul class="contact-list">
      <li><span class="label">w</span>: www.marloweconcierge-demo.net</li>
      <li><span class="label">e</span>: peter@marloweconcierge-demo.net</li>
      <li><span class="label">m</span>: 0412 907 281</li>
    </ul>
  </main>
</body>
</html>
```